Kestrel Electrical Business Card

We need a business card design for our family-run electrical contracting business based in Western Australia called 'Kestrel Electrical'. We provide electrical services including residential, commercial and industrial. We aim for individual business cards to be made for all of our employees. We already have a company logo, which we require to be featured on the design. We would like simple, sleek and vibrant designs, which incorporate our logo and represent our business. We do not want anything involving too many graphics/images. We like the colours red, black, white and all shades of grey. The final design should communicate professionalism and trustworthiness.
We require the following contact information:
Name- Owen Strickland
EC 5809
Mobile number- 0455 918 302
Fax number (including area code)- (08) 9640 2718
Email adress- name@kestrelelectrical.example
Electrical
- ITC Handel Bold

```html
<!DOCTYPE html>
<html lang="en">
<head>
<meta charset="utf-8">
<title>Kestrel Electrical – Business Card Concepts</title>
<link rel="stylesheet" href="https://fonts.googleapis.com/css2?family=Quicksand:wght@400;500;600&display=swap">
<style>
  :root {
    --canvas: #ffffff;
    --label-grey: #a3a3a3;
    --rule-grey: #d6d6d6;
    --card-border: #cfcfcf;
    --brand-red: #e2191b;
    --ink: #3a3a3a;
    --ink-soft: #6a6a6a;
    --white: #ffffff;
  }
  * { margin: 0; padding: 0; box-sizing: border-box; }
  html, body { width: 1200px; height: 800px; overflow: hidden; }
  body {
    position: relative;
    background: var(--canvas);
    font-family: "Quicksand", sans-serif;
    color: var(--ink);
  }
  .option-label {
    position: absolute;
    top: 68px;
    font-size: 48px;
    font-weight: 400;
    color: var(--label-grey);
    transform: translateX(-50%);
    line-height: 1;
  }
  .option-label--a { left: 336px; }
  .option-label--b { left: 865px; }
  .options-divider {
    position: absolute;
    left: 602px; top: 158px;
    width: 1px; height: 267px;
    background: var(--rule-grey);
  }
  .card {
    position: absolute;
    top: 200px;
    width: 336px; height: 197px;
    background: var(--white);
    border: 1px solid var(--card-border);
    overflow: hidden;
  }
  .card--a { left: 168px; }
  .card--b { left: 702px; }
  .card * { position: absolute; white-space: nowrap; }

  .brand {
    display: flex; align-items: center; gap: 3px;
    font-size: 8.5px; font-weight: 600; letter-spacing: 0.3px;
    color: var(--ink); text-transform: uppercase; line-height: 1;
  }
  .brand__mark {
    position: static;
    width: 8px; height: 8px;
    background: var(--brand-red);
  }
  .brand-wrap { position: absolute; }
  .card--a .brand { left: 9px; top: 17px; }
  .card--b .brand { left: 23px; top: 17px; }

  .address {
    font-size: 6px; line-height: 8px; letter-spacing: 0.3px;
    color: var(--ink-soft); text-transform: uppercase;
  }
  .card--a .address { left: 11px; top: 160px; }
  .card--b .address { left: 26px; top: 160px; }

  .card__panel {
    left: 130px; top: 0;
    width: 206px; height: 197px;
    background: var(--brand-red);
  }
  .name {
    font-weight: 500; text-transform: uppercase; letter-spacing: 0.4px;
  }
  .job-title {
    text-transform: uppercase; letter-spacing: 0.4px;
  }
  .card--a .name { left: 165px; top: 42px; font-size: 13px; color: var(--white); }
  .card--a .job-title { left: 165px; top: 61px; font-size: 9.5px; color: var(--white); }
  .card--a .panel-rule {
    left: 165px; top: 97px; width: 119px; height: 1px;
    background: rgba(255,255,255,0.35);
  }
  .contact { line-height: 10.5px; letter-spacing: 0.3px; text-transform: uppercase; }
  .contact span { position: static; }
  .contact__key { font-size: 6px; }
  .card--a .contact { left: 165px; top: 123px; font-size: 8.5px; color: var(--white); }

  .card--b .column-rule {
    left: 120px; top: 37px; width: 1px; height: 119px;
    background: var(--card-border);
  }
  .card--b .name { left: 164px; top: 38px; font-size: 12.5px; color: var(--ink); font-weight: 400; }
  .card--b .job-title { left: 164px; top: 60px; font-size: 9px; color: var(--ink-soft); }
  .card--b .contact { left: 164px; top: 129px; font-size: 6px; line-height: 8px; color: var(--ink-soft); }
</style>
</head>
<body>
  <div class="option-label option-label--a">A</div>
  <div class="option-label option-label--b">B</div>
  <div class="options-divider"></div>

  <section class="card card--a" aria-label="Business card option A">
    <div class="brand"><i class="brand__mark"></i>Kestrel Electrical</div>
    <p class="address">Your company<br>Address goes here<br>Australia</p>
    <div class="card__panel"></div>
    <h2 class="name">Owen Strickland</h2>
    <p class="job-title">Job title</p>
    <div class="panel-rule"></div>
    <p class="contact">
      <span class="contact__key">Phone:</span> 0455 918 302<br>
      <span class="contact__key">Fax:</span> (08) 9640 2718<br>
      <span class="contact__key">Email:</span> <span class="contact__key">name@kestrelelectrical.example</span>
    </p>
  </section>

  <section class="card card--b" aria-label="Business card option B">
    <div class="brand"><i class="brand__mark"></i>Kestrel Electrical</div>
    <p class="address">Your company<br>Address goes here<br>Australia</p>
    <div class="column-rule"></div>
    <h2 class="name">Owen Strickland</h2>
    <p class="job-title">Job title</p>
    <p class="contact">
      Phone: 0455 918 302<br>
      Fax: (08) 9640 2718<br>
      Email: name@kestrelelectrical.example
    </p>
  </section>
</body>
</html>
```